VelliFilez Website

VelliFiles - Orderly Medical Filez
We need a Web design for a new company called - VelliFilez.
VelliFilez is a Personal Injury and Medical Record Legal Service Outsourcing company. We help Personal Injury Attorneys - with fact based Medical Chronologies and Summaries.

We take Medical Records in disarray and put them in order and summarize them in a chronological order and Update them as needed (if more medical records are added)
Take Releases (for medical records) and work with doctor practices and get the records if needed

Target Market(s)

Personal Injury Attorneys

Industry/Entity Type

Attorney

Number of Pages Required

2 page

Font styles to use
Serif
Sans Serif

Colors

Designer to choose colors to be used in the design.

Requirements
Must have
• Professional Design
• Just need the design for the Home page and Internal pages - I will do the Coding for the pages in html and/or wordpress.
• Don't worry about the content - just need a design.

```html
<!DOCTYPE html>
<html lang="en">
<head>
<meta charset="utf-8">
<title>VelliFilez – Home</title>
<link href="https://fonts.googleapis.com/css2?family=Montserrat:wght@700&family=Open+Sans:wght@300;400;600;700&display=swap" rel="stylesheet">
<style>
  :root {
    --navy: #0b2a6b;
    --nav-band: rgba(74, 108, 168, 0.82);
    --action-blue: #2b6cc4;
    --text-grey: #555a63;
    --heading-grey: #5c6068;
    --brand-grey: #3a3f48;
    --white: #ffffff;
    --hero-light: #e4e9f1;
    --hero-mid: #b8c4d6;
  }
  * { margin: 0; padding: 0; box-sizing: border-box; }
  html, body { width: 768px; height: 1200px; overflow: hidden; background: var(--white); }
  body { position: relative; font-family: "Open Sans", sans-serif; color: var(--text-grey); }

  .hero { position: absolute; left: 0; top: 0; width: 768px; height: 432px; }
  .hero-photo {
    position: absolute; inset: 0;
    background: linear-gradient(120deg, var(--hero-mid) 0%, var(--hero-light) 45%, #f1f3f7 70%, var(--hero-mid) 100%);
  }
  .brand {
    position: absolute; left: 80px; top: 0; width: 138px; height: 77px;
    background: var(--white);
    display: flex; align-items: center; justify-content: center; gap: 7px;
  }
  .brand-mark { width: 10px; height: 10px; border-radius: 50%; background: var(--brand-grey); }
  .brand-name { font-family: "Open Sans", sans-serif; font-weight: 600; font-size: 17px; color: var(--brand-grey); }

  .main-nav {
    position: absolute; left: 0; top: 84px; width: 768px; height: 37px;
    background: var(--nav-band);
  }
  .main-nav a {
    position: absolute; top: 10px;
    font-family: "Montserrat", sans-serif; font-weight: 700; font-size: 14px;
    color: var(--white); text-decoration: none; white-space: nowrap;
  }

  .hero-lead {
    position: absolute; left: 20px; top: 209px; width: 728px;
    text-align: center; font-family: "Montserrat", sans-serif; font-weight: 700;
    font-size: 19px; line-height: 29px; color: var(--white);
    text-shadow: 0 1px 4px rgba(0,0,0,0.45);
  }
  .call-button {
    position: absolute; left: 288px; top: 299px; width: 193px; height: 55px;
    background: var(--navy); color: var(--white);
    font-family: "Open Sans", sans-serif; font-weight: 700; font-size: 35px;
    display: flex; align-items: center; justify-content: center; letter-spacing: 0.5px;
  }

  .about-title {
    position: absolute; left: 0; top: 446px; width: 768px; text-align: center;
    font-weight: 400; font-size: 19px; color: var(--heading-grey);
  }
  .about-intro {
    position: absolute; left: 86px; top: 497px; width: 598px;
    font-size: 9.4px; line-height: 11.6px; font-weight: 300;
  }

  .feature { position: absolute; width: 290px; }
  .feature-photo { width: 290px; height: 194px; }
  .feature-text { position: absolute; left: 0; width: 256px; font-size: 9.2px; line-height: 11.5px; font-weight: 300; }
  .feature-more {
    position: absolute; right: 0; width: 32px; height: 33px; border-radius: 4px;
    background: var(--action-blue);
  }

  .site-footer {
    position: absolute; left: 0; top: 1163px; width: 768px; height: 37px;
    background: var(--navy); color: var(--white); font-size: 7.5px;
  }
  .site-footer .copyright { position: absolute; left: 86px; top: 13px; }
  .site-footer .social { position: absolute; left: 340px; top: 14px; display: flex; gap: 13px; }
  .site-footer .social span { width: 8px; height: 8px; border-radius: 50%; background: var(--white); display: block; }
  .site-footer .legal-link { position: absolute; top: 13px; color: var(--white); text-decoration: none; }
</style>
</head>
<body>

<header class="hero">
  <div class="hero-photo" role="img" aria-label="Doctor in a white coat with a stethoscope using a tablet"></div>

  <div class="brand">
    <span class="brand-mark"></span><span class="brand-name">VelliFilez</span>
  </div>

  <nav class="main-nav">
    <a href="#" style="left:21px">ABOUT US</a>
    <a href="#" style="left:125px">OUR TEAM</a>
    <a href="#" style="left:224px">SERVICES</a>
    <a href="#" style="left:324px">FAQ</a>
    <a href="#" style="left:374px">CUSTOMER STORIES</a>
    <a href="#" style="left:558px">CAREERS</a>
    <a href="#" style="left:675px">CONTACT</a>
  </nav>

  <p class="hero-lead">VelliFilez, Lorem ipsum dolor sit amet, lacinia leo, morbi eget sapien<br>eleifend tincidunt proin. Mi aliquam eget.</p>
  <a class="call-button">CALL US</a>
</header>

<main>
  <h2 class="about-title">About Us</h2>
  <p class="about-intro">Lorem ipsum dolor sit amet, lacinia leo, morbi eget sapien eleifend tincidunt proin. Mi aliquam eget. Tristique lectus risus commodo non ac, ut eu eget, mi pede nonummy arcu vehicula, adipiscing eleifend. Molestie integer, dolor eu sed risus. Porttitor egestas purus, eros diam lacus in tincidunt ipsum nonummy, hendrerit dictum cras, eleifend convallis, congue mauris tempor dictum velit et et. Tellus justo pede egestas rutrum wisi amet. At volutpat et ipsum proin, elit lectus cras arcu, vitae sit vel tellus, egestas dui.</p>

  <article class="feature" style="left:82px; top:564px;">
    <div class="feature-photo" role="img" aria-label="Doctor holding a patient file in front of shelves of records" style="background:linear-gradient(90deg,#c9a77a,#e8e2d8 50%,#c09a6c)"></div>
    <p class="feature-text" style="top:209px">Lorem ipsum dolor sit amet, lacinia leo, morbi eget sapien eleifend tincidunt proin. Mi aliquam eget. Tristique lectus risus commodo non ac, ut eu eget, mi pede nonummy arcu vehicula, adipiscing eleifend. Molestie integer, dolor eu sed risus.</p>
    <a class="feature-more" style="top:200px"><svg width="32" height="33" viewBox="0 0 32 33"><path d="M9 10l7 6.5-7 6.5M16 10l7 6.5-7 6.5" fill="none" stroke="#fff" stroke-width="2.6"/></svg></a>
  </article>

  <article class="feature" style="left:386px; top:564px;">
    <div class="feature-photo" role="img" aria-label="Nurse in blue scrubs writing on a tablet" style="background:linear-gradient(110deg,#7fa6d6,#b6cde8 55%,#eef1f5)"></div>
    <p class="feature-text" style="top:209px">Lorem ipsum dolor sit amet, lacinia leo, morbi eget sapien eleifend tincidunt proin. Mi aliquam eget. Tristique lectus risus commodo non ac, ut eu eget, mi pede nonummy arcu vehicula, adipiscing eleifend. Molestie integer, dolor eu sed risus.</p>
    <a class="feature-more" style="top:200px"><svg width="32" height="33" viewBox="0 0 32 33"><path d="M9 10l7 6.5-7 6.5M16 10l7 6.5-7 6.5" fill="none" stroke="#fff" stroke-width="2.6"/></svg></a>
  </article>

  <article class="feature" style="left:82px; top:870px;">
    <div class="feature-photo" role="img" aria-label="Long corridor of open filing cabinets" style="background:linear-gradient(100deg,#5a6f9a,#8ea2c8 50%,#3c4d78)"></div>
    <p class="feature-text" style="top:209px">Lorem ipsum dolor sit amet, lacinia leo, morbi eget sapien eleifend tincidunt proin. Mi aliquam eget. Tristique lectus risus commodo non ac, ut eu eget, mi pede nonummy arcu vehicula, adipiscing eleifend. Molestie integer, dolor eu sed risus.</p>
    <a class="feature-more" style="top:200px"><svg width="32" height="33" viewBox="0 0 32 33"><path d="M9 10l7 6.5-7 6.5M16 10l7 6.5-7 6.5" fill="none" stroke="#fff" stroke-width="2.6"/></svg></a>
  </article>

  <article class="feature" style="left:386px; top:870px;">
    <div class="feature-photo" role="img" aria-label="Medical staff typing on a keyboard" style="background:linear-gradient(180deg,#4f8fd0,#c9d9ec 55%,#2a3446)"></div>
    <p class="feature-text" style="top:209px">Lorem ipsum dolor sit amet, lacinia leo, morbi eget sapien eleifend tincidunt proin. Mi aliquam eget. Tristique lectus risus commodo non ac, ut eu eget, mi pede nonummy arcu vehicula, adipiscing eleifend. Molestie integer, dolor eu sed risus.</p>
    <a class="feature-more" style="top:200px"><svg width="32" height="33" viewBox="0 0 32 33"><path d="M9 10l7 6.5-7 6.5M16 10l7 6.5-7 6.5" fill="none" stroke="#fff" stroke-width="2.6"/></svg></a>
  </article>
</main>

<footer class="site-footer">
  <span class="copyright">© Copyright 2018 VelliFilez All Rights Reserved.</span>
  <div class="social"><span></span><span></span><span></span><span></span><span></span></div>
  <a class="legal-link" href="#" style="left:600px">Privacy</a>
  <a class="legal-link" href="#" style="left:658px">Terms</a>
</footer>

</body>
</html>
```